Flyer for American Indian Elders on Dementia Warning Signs

We need a flyer designed for older adults who are American Indian or Alaska Native (in the U.S.).

Ideally, the flyer should complement the colors of our logos. The project logo and our organization logo are attached to the brief.

When people see the flyer we want them to feel that it represents their culture, is warm, and professional but relatable to older adults and people who have limited incomes.

I have attached an earlier draft of the document we designed ourselves BUT we want different and better.

It is for older adults who have trouble reading so:
1. you must use a font that is 11.5 points or larger
2. Do not put text over complex pictures or use shading with words
3. You can use a serif font for the heading, but should use san serif for the body text
4. There should be good contrast between the font color and background

Please do not use any images that include a head dress or pictures of American Indian people or things that are very traditional or "token" imagery.

We need to save a small space under the call out box/ somewhere on the flyer for other people to add their logo once they download.

Let us know if you have questions or need additional information.

Target Market(s)

Older American Indian people

Font styles to use
Serif
Sans Serif

Requirements
Must have
• Easy to read for older adults
Should not have
• indian headdress

```html
<!DOCTYPE html>
<html lang="en">
<head>
<meta charset="utf-8">
<title>10 Signs of Thinking or Memory Changes that Might be Dementia</title>
<link href="https://fonts.googleapis.com/css2?family=PT+Sans:wght@400;700&family=PT+Sans+Narrow:wght@400;700&display=swap" rel="stylesheet">
<style>
  :root {
    --ink: #000000;
    --paper: #ffffff;
    --clay: #9a1b1f;
    --teal: #3a9aa2;
    --sky: #29abe2;
    --sun: #f7e01c;
    --sand-light: #d9c2a4;
    --sand-dark: #8f7660;
    --rule: #bdbdbd;
  }
  * { box-sizing: border-box; margin: 0; padding: 0; }
  html, body { width: 855px; height: 1200px; overflow: hidden; background: var(--paper); }
  body { font-family: "PT Sans", Arial, sans-serif; }
  .flyer { position: relative; width: 855px; height: 1200px; overflow: hidden; background: var(--paper); }

  /* left column */
  .intro-panel { position: absolute; left: 0; top: 0; width: 419px; height: 1083px; background: var(--paper); }
  .intro-panel svg.wave { position: absolute; left: 0; top: 0; width: 419px; height: 1083px; }
  .brand { position: absolute; left: 22px; top: 28px; display: flex; align-items: center; gap: 12px; }
  .brand-dot { width: 58px; height: 58px; border-radius: 50%; background: var(--teal); flex: none; }
  .brand-name { color: var(--teal); font-weight: 700; font-size: 19px; line-height: 1.1; text-transform: uppercase; width: 300px; }

  .title { position: absolute; left: 48px; top: 200px; width: 360px; color: var(--paper); font-weight: 700; font-size: 30px; line-height: 1.12; }
  .title-number { color: var(--sun); font-size: 52px; line-height: 0.9; vertical-align: -4px; }

  .intro-text { position: absolute; left: 36px; width: 372px; color: var(--paper); font-size: 15.5px; line-height: 1.35; }
  .intro-text.highlight { color: var(--sun); font-weight: 700; font-size: 16.5px; }

  .photo-area { position: absolute; left: 0; top: 817px; width: 419px; height: 266px;
    background: radial-gradient(ellipse at 35% 40%, var(--sand-light), var(--sand-dark) 95%); }

  .footer { position: absolute; left: 0; top: 1083px; width: 419px; height: 117px; background: var(--ink); color: var(--paper);
    padding: 22px 28px 0 34px; font-size: 14.5px; line-height: 1.3; }
  .footer-link { display: block; color: var(--sun); font-size: 16px; text-align: center; margin-top: 6px; }

  /* right column */
  .signs { position: absolute; left: 419px; top: 0; width: 436px; height: 1200px; background: var(--ink); }
  .sign { position: absolute; left: 20px; width: 410px; color: var(--paper); }
  .sign-number { position: absolute; left: 0; top: -2px; color: var(--sun); font-weight: 700; font-size: 22px; }
  .sign-body { margin-left: 36px; }
  .sign-title { color: var(--sky); font-family: "PT Sans Narrow", "Arial Narrow", sans-serif; font-weight: 700; font-size: 15.5px; text-transform: uppercase; line-height: 1.2; }
  .sign-title .plain { text-transform: none; font-weight: 400; font-size: 16px; }
  .sign-lead { font-size: 14.5px; line-height: 1.3; }
  .sign-lead.bold { font-family: "PT Sans Narrow", "Arial Narrow", sans-serif; font-size: 16px; }
  .sign-list { list-style: none; margin-left: -12px; }
  .sign-list li { position: relative; padding-left: 24px; font-size: 14.5px; line-height: 1.3; }
  .sign-list li::before { content: ""; position: absolute; left: 2px; top: 7px; width: 7px; height: 7px; border-radius: 50%; background: var(--sky); }
  .sign-list li.continued::before { display: none; }

  .logo-slot { position: absolute; left: 461px; top: 1083px; width: 377px; height: 97px; background: var(--paper); border: 1px solid var(--rule);
    display: flex; align-items: center; padding: 0 20px; }
  .partner { display: flex; align-items: center; gap: 8px; width: 190px; }
  .partner-mark { width: 30px; height: 30px; background: var(--teal); flex: none; }
  .partner-name { color: var(--teal); font-weight: 700; font-size: 12px; line-height: 1.15; text-transform: uppercase; }
  .logo-slot-label { flex: 1; text-align: center; font-weight: 700; font-size: 15.5px; line-height: 1.3; color: var(--ink); text-transform: uppercase; }
</style>
</head>
<body>
<main class="flyer">

  <section class="intro-panel">
    <svg class="wave" viewBox="0 0 419 1083" preserveAspectRatio="none" aria-hidden="true">
      <path d="M0 175 C 90 150, 140 120, 230 120 C 320 120, 370 155, 419 140 L 419 1083 L 0 1083 Z" fill="var(--clay)"/>
    </svg>

    <div class="brand">
      <span class="brand-dot"></span>
      <span class="brand-name">Four Rivers Center for Brain Health</span>
    </div>

    <h1 class="title"><span class="title-number">10</span> Signs of&nbsp; Thinking or Memory Changes that Might be Dementia</h1>

    <p class="intro-text" style="top:346px">As we get older, we may slow down a bit. This is a normal part of aging. Changes in memory or thinking that make it harder to get through the day, are normal part of aging. These may be early signs of dementia.</p>
    <p class="intro-text highlight" style="top:480px">American Indian and Alaska Native people have a high risk of dementia</p>
    <p class="intro-text" style="top:564px">Big changes in memory or thinking that make it hard to get through the day are not a normal part of aging</p>
    <p class="intro-text" style="top:648px">People with one or more of these 10 signs should talk to their doctor to find the cause. It is not always dementia.</p>
    <p class="intro-text" style="top:736px">Early dementia diagnosis gives you a chance to get care and plan your future.</p>
  </section>

  <div class="photo-area" role="img" aria-label="Photograph of footprints walking across soft beach sand"></div>

  <footer class="footer">
    To learn more about the warning signs of dementia in American Indian and Alaska Native people, visit:
    <span class="footer-link">www.fourriversbrainhealth.org</span>
  </footer>

  <section class="signs">
    <div class="sign" style="top:52px">
      <span class="sign-number">1</span>
      <div class="sign-body">
        <h2 class="sign-title">Memory loss that affects your daily life.</h2>
        <p class="sign-lead">You may:</p>
        <ul class="sign-list">
          <li>Forget events or important dates.</li>
          <li>Repeat yourself.</li>
          <li>Rely more often on lists or sticky notes to remember things.</li>
        </ul>
      </div>
    </div>

    <div class="sign" style="top:172px">
      <span class="sign-number">2</span>
      <div class="sign-body">
        <h2 class="sign-title">Trouble planning or solving problems.</h2>
        <p class="sign-lead">You may have a harder time:</p>
        <ul class="sign-list">
          <li>Paying bills.</li>
          <li>Cooking recipes you have used for years.</li>
        </ul>
      </div>
    </div>

    <div class="sign" style="top:268px">
      <span class="sign-number">3</span>
      <div class="sign-body">
        <h2 class="sign-title">Get confused about the time, date, or where you are.</h2>
      </div>
    </div>

    <div class="sign" style="top:328px">
      <span class="sign-number">4</span>
      <div class="sign-body">
        <h2 class="sign-title">Daily tasks are getting harder, <span class="plain">including:</span></h2>
        <ul class="sign-list">
          <li>Driving.</li>
          <li>Making a grocery list or going shopping.</li>
        </ul>
      </div>
    </div>

    <div class="sign" style="top:410px">
      <span class="sign-number">5</span>
      <div class="sign-body">
        <h2 class="sign-title">Trouble with how your eyesight and thinking work together that gets worse.</h2>
        <p class="sign-lead bold">This includes:</p>
        <ul class="sign-list">
          <li>Tripping, falls, or problems with your balance.</li>
          <li>Spilling or dropping things more.</li>
        </ul>
      </div>
    </div>

    <div class="sign" style="top:536px">
      <span class="sign-number">6</span>
      <div class="sign-body">
        <h2 class="sign-title">New trouble talking or writing.</h2>
        <ul class="sign-list">
          <li>You have a hard time finding the words you want to say. For example, you may say “that thing on your wrist that tells time” instead of “watch.”</li>
        </ul>
      </div>
    </div>

    <div class="sign" style="top:636px">
      <span class="sign-number">7</span>
      <div class="sign-body">
        <h2 class="sign-title">Lose and cannot find things.</h2>
        <p class="sign-lead">&nbsp;For example, you:</p>
        <ul class="sign-list">
          <li>Can’t find the coffee pot that you use every day.</li>
          <li>Might put your car keys in the freezer.</li>
        </ul>
      </div>
    </div>

    <div class="sign" style="top:742px">
      <span class="sign-number">8</span>
      <div class="sign-body">
        <h2 class="sign-title">Notice changes in mood or personality, <span class="plain">such as being:</span></h2>
        <ul class="sign-list">
          <li>Easily mad or sad in everyday situations.</li>
          <li class="continued">More fearful (scared) or suspicious (not trusting).</li>
        </ul>
      </div>
    </div>

    <div class="sign" style="top:846px">
      <span class="sign-number">9</span>
      <div class="sign-body">
        <h2 class="sign-title">Act different and make poor choices.</h2>
        <p class="sign-lead">This may make you more likely to:</p>
        <ul class="sign-list">
          <li>Spend money you do not have or be a scam victim.</li>
          <li>Stop washing up regularly or pay less attention to how you look.</li>
          <li>Forget to take care of your pet.</li>
        </ul>
      </div>
    </div>

    <div class="sign" style="top:986px">
      <span class="sign-number">10</span>
      <div class="sign-body">
        <h2 class="sign-title">Pull away from friends and family, <span class="plain">because it is harder to keep up.</span></h2>
        <ul class="sign-list">
          <li>You may not want to do things you used to enjoy, like sporting events, church, music, or sex.</li>
        </ul>
      </div>
    </div>
  </section>

  <aside class="logo-slot">
    <div class="partner">
      <span class="partner-mark"></span>
      <span class="partner-name">Circle of Elders Network</span>
    </div>
    <p class="logo-slot-label">Place your<br>logo here</p>
  </aside>

</main>
</body>
</html>
```